Design & Build a WordPress Website for “Coastline Stillness” (Australian Charity Rebrand)

We are a registered Australian charity currently known as Veluna Meditation Australia.

We are rebranding our public identity to “Coastline Stillness” to make the meditation practice easier to understand and more relatable for people in Australia and New Zealand.

We are looking for an experienced WordPress designer + developer to design and build a complete website that reflects:

Peace

Trust

Authentic Himalayan roots

Simplicity

Spiritual depth without being religious

Warmth, friendliness, and community feeling

This is not a corporate website. This is a meditation movement website for a non-profit organisation.

Target Market(s)

Australia and New Zealand - Age 25-65

Industry/Entity Type

Not of profit meditation organisation

Requirements
Must have
• Included in the design brief attached
Nice to have
Should not have

```html
<!DOCTYPE html>
<html lang="en">
<head>
<meta charset="UTF-8">
<title>Coastline Stillness</title>
<link href="https://fonts.googleapis.com/css2?family=Montserrat:wght@500;600;700;800&family=Open+Sans:wght@400;600&display=swap" rel="stylesheet">
<style>
:root{
  --green:#1f5a44;
  --green-dark:#164434;
  --tan:#d6a774;
  --orange:#d98a3a;
  --ink:#1c1c1c;
  --text:#3a3a3a;
  --muted:#f3f1ee;
  --footer:#121212;
  --white:#ffffff;
}
*{box-sizing:border-box;margin:0;padding:0}
html,body{width:1200px;height:5040px;overflow:hidden;background:var(--white)}
body{font-family:"Open Sans",sans-serif;color:var(--text);position:relative}
h1,h2,h3,.nav,.btn{font-family:"Montserrat",sans-serif}
.abs{position:absolute}
.btn{position:absolute;display:inline-flex;align-items:center;justify-content:center;border-radius:22px;background:var(--green);color:#fff;font-size:15px;font-weight:600;height:40px;padding:0 26px;white-space:nowrap}
.btn.tan{background:var(--tan)}
.section-title{position:absolute;left:0;width:1200px;text-align:center;font-size:46px;font-weight:700;color:var(--ink)}
.underline{position:absolute;left:570px;width:60px;height:4px;background:var(--tan);border-radius:2px}

/* hero */
.hero{position:absolute;left:0;top:0;width:1200px;height:720px;overflow:hidden}
.hero-photo{position:absolute;inset:0;background:linear-gradient(180deg,#8fa8b8 0%,#6f8a7c 35%,#3d5a3a 65%,#22331f 100%)}
.hero-shade{position:absolute;inset:0;background:linear-gradient(90deg,rgba(0,0,0,.45),rgba(0,0,0,.05) 60%)}
.navbar{position:absolute;left:60px;top:22px;width:1080px;height:80px;background:rgba(255,255,255,.2);border-radius:14px;z-index:2}
.brand{position:absolute;left:24px;top:20px;color:#fff;font-family:"Montserrat",sans-serif;font-weight:700;font-size:20px;line-height:1.1;display:flex;align-items:center;gap:12px}
.brand .dot{width:36px;height:36px;border-radius:50%;background:rgba(255,255,255,.35)}
.brand small{display:block;font-size:11px;letter-spacing:3px;font-weight:700}
.nav{position:absolute;left:560px;top:30px;display:flex;gap:26px;font-size:15px;font-weight:600;color:#fff;white-space:nowrap}
.nav .active{color:var(--green);border-bottom:2px solid var(--green);padding-bottom:4px}
.pill{position:absolute;top:23px;width:54px;height:34px;border-radius:17px;font:700 14px "Montserrat",sans-serif;display:flex;align-items:center;justify-content:center;color:#fff}
.hero h1{position:absolute;left:60px;top:190px;color:#fff;font-size:54px;font-weight:800;line-height:1.1;width:600px}
.hero p{position:absolute;left:60px;top:330px;color:#fff;font-size:21px;line-height:1.45;width:560px}
.dots{position:absolute;left:560px;top:596px;display:flex;gap:10px}
.dots span{width:22px;height:5px;background:rgba(255,255,255,.5);border-radius:3px}
.dots span:first-child{background:#fff}

/* how it works */
.step{position:absolute;top:930px;width:320px;height:400px;border-radius:10px;background:var(--muted)}
.step.feature{background:var(--green);top:910px;height:430px}
.step .photo{position:absolute;left:14px;top:14px;width:292px;height:160px;border-radius:8px}
.step h3{position:absolute;left:24px;font-size:26px;font-weight:600;color:var(--orange)}
.step p{position:absolute;left:24px;width:272px;font-size:16px;line-height:1.5}
.step .more{position:absolute;left:24px;font-size:15px;font-weight:600;color:var(--green);border-bottom:1px solid var(--green)}
.feature h3,.feature p,.feature .more{color:#fff;border-color:#fff}

/* events */
.event{position:absolute;width:320px;height:200px;border-radius:10px;background:var(--muted);box-shadow:0 4px 14px rgba(0,0,0,.08)}
.event.dark{background:var(--green)}
.event h3{position:absolute;left:24px;top:24px;font-size:20px;font-weight:600;color:var(--orange)}
.event.dark h3,.event.dark p{color:#fff}
.event p{position:absolute;left:24px;top:62px;width:260px;font-size:15px;line-height:1.5}
.event .btn{left:24px;top:130px;height:36px;font-size:14px;padding:0 22px}

/* support */
.support-card{position:absolute;left:420px;top:2720px;width:670px;height:310px;background:#fff;border-radius:14px;box-shadow:0 8px 30px rgba(0,0,0,.2)}
.support-card h2{position:absolute;left:0;width:670px;top:40px;text-align:center;font-size:44px;font-weight:700;color:var(--ink)}
.support-card p{position:absolute;left:70px;width:530px;top:120px;text-align:center;font-size:16px;line-height:1.5}

/* footer */
.footer{position:absolute;left:0;top:4440px;width:1200px;height:600px;background:var(--footer);color:#e8e8e8}
.footer h4{font:700 20px "Montserrat",sans-serif;color:#fff;position:absolute}
.footer .col{position:absolute;font-size:14px;line-height:2.5}
.footer .rule{position:absolute;left:110px;width:980px;height:1px;background:#3a3a3a}
</style>
</head>
<body>

<!-- Hero -->
<section class="hero">
  <div class="hero-photo" role="img" aria-label="Person with arms raised facing a mountain lake at sunrise"></div>
  <div class="hero-shade"></div>
  <header class="navbar">
    <div class="brand"><span class="dot"></span><span>VELUNA<small>MEDITATION</small></span></div>
    <nav class="nav"><span class="active">Home</span><span>What is Coastline Stillness</span><span>About US</span><span>More ⌄</span></nav>
    <span class="pill" style="left:936px;background:var(--green)">AU</span>
    <span class="pill" style="left:1000px;background:var(--tan)">NZ</span>
  </header>
  <h1>A SIMPLE PATH TO INNER PEACE.</h1>
  <p>Coastline Stillness is a natural, non-religious meditation practice taught freely to help reduce stress, quiet the mind, and reconnect with yourself.</p>
  <span class="btn" style="left:60px;top:472px">Find a Session</span>
  <span class="btn tan" style="left:242px;top:472px">Try Meditation</span>
  <div class="dots"><span></span><span></span><span></span></div>
</section>

<!-- How it works -->
<h2 class="section-title" style="top:760px">How It Works</h2>
<div class="underline" style="top:826px"></div>

<article class="step" style="left:110px">
  <div class="photo" role="img" aria-label="Group meditating indoors" style="background:linear-gradient(135deg,#8a6a52,#4a3a30)"></div>
  <h3 style="top:196px">Learn</h3>
  <p style="top:240px">Our instructors guide you through a natural Coastline Stillness practice that is easy to learn and</p>
  <span class="more" style="top:350px">Read More ...</span>
</article>
<article class="step feature" style="left:440px">
  <h3 style="top:26px;color:#fff">Practice</h3>
  <p style="top:72px">Join free group sessions — in person or online — and meditate in a calm, supportive community.</p>
  <span class="more" style="top:170px">Read More ...</span>
  <div class="photo" role="img" aria-label="People meditating together" style="top:250px;height:164px;background:linear-gradient(135deg,#7a6048,#3a2e26);border:3px solid #fff"></div>
</article>
<article class="step" style="left:770px">
  <div class="photo" role="img" aria-label="Woman meditating in a bright room" style="background:linear-gradient(135deg,#c06a40,#6a3a28)"></div>
  <h3 style="top:196px">Feel</h3>
  <p style="top:240px">With regular practice, many people experience more clarity, emotional balance, and inner peace in everyday</p>
  <span class="more" style="top:350px">Read More ...</span>
</article>

<!-- What is -->
<div class="abs" role="img" aria-label="Illustration of a person meditating with a lotus" style="left:110px;top:1410px;width:320px;height:320px;border-radius:10px;background:linear-gradient(160deg,#fbe3d3,#f4b48e)"></div>
<div class="abs" role="img" aria-label="Small illustration of a meditating figure" style="left:440px;top:1408px;width:110px;height:110px;border-radius:50%;background:#e8eef5"></div>
<div class="abs" role="img" aria-label="Woman meditating outdoors" style="left:360px;top:1590px;width:200px;height:260px;border:5px solid #fff;border-radius:8px;background:linear-gradient(180deg,#9db6cf,#5c7a8e);box-shadow:0 6px 18px rgba(0,0,0,.15)"></div>
<h2 class="abs" style="left:660px;top:1410px;font-size:44px;font-weight:700;color:var(--ink);line-height:1.15;width:440px">What Is Coastline Stillness</h2>
<div class="abs" style="left:660px;top:1530px;width:60px;height:4px;background:var(--tan)"></div>
<p class="abs" style="left:660px;top:1556px;width:430px;font-size:15px;line-height:1.6">Coastline Stillness is a simple, natural meditation practice rooted in the Himalayan tradition. It helps quiet the mind, reduce stress, and bring a sense of inner calm and clarity. The technique is easy to learn, requires no prior experience or belief system, and is taught freely in a warm, supportive community environment.</p>
<p class="abs" style="left:660px;top:1736px;width:430px;font-size:15px;line-height:1.6">The practice is taught freely in a calm, supportive environment and is suitable for people of all ages and backgrounds.</p>
<span class="btn" style="left:660px;top:1826px">Read More</span>

<!-- Events -->
<h2 class="section-title" style="top:1980px">Events &amp; Programs</h2>
<div class="underline" style="top:2044px"></div>
<div class="abs" role="img" aria-label="Illustration of a woman meditating among stars" style="left:440px;top:2080px;width:320px;height:420px;border-radius:10px;background:linear-gradient(180deg,#a7bcd8,#e3b24a)"></div>
<article class="event" style="left:110px;top:2080px"><h3>Events &amp; Programs 1</h3><p>Lorem ipsum dolor sit amet, consec tetur adipiscing elit, sed do</p><span class="btn">Read More</span></article>
<article class="event" style="left:110px;top:2300px"><h3>Events &amp; Programs 2</h3><p>Lorem ipsum dolor sit amet, consec tetur adipiscing elit, sed do</p><span class="btn">Read More</span></article>
<article class="event dark" style="left:770px;top:2080px"><h3>Events &amp; Programs 3</h3><p>Lorem ipsum dolor sit amet, consec tetur adipiscing elit, sed do</p><span class="btn tan">Read More</span></article>
<article class="event" style="left:770px;top:2300px"><h3>Events &amp; Programs 4</h3><p>Lorem ipsum dolor sit amet, consec tetur adipiscing elit, sed do</p><span class="btn">Read More</span></article>

<!-- Support -->
<section class="abs" role="img" aria-label="Man sitting by a misty mountain lake" style="left:0;top:2620px;width:1200px;height:480px;background:linear-gradient(90deg,#2f3a30,#6d7c74 50%,#aab6b4)"></section>
<div class="support-card">
  <h2>Support Our Work</h2>
  <p>Your donation helps us offer free meditation sessions, grow community programs, and create peaceful spaces for people to reconnect with themselves.</p>
  <span class="btn" style="left:286px;top:228px">Donate</span>
  <div class="abs" role="img" aria-label="Small meditating figure in a wreath" style="left:530px;top:200px;width:100px;height:100px;border-radius:50%;background:#eef0e4"></div>
</div>

<!-- Volunteer -->
<section class="abs" role="img" aria-label="Layered misty mountain ranges" style="left:0;top:3360px;width:1200px;height:420px;background:linear-gradient(180deg,#ffffff 0%,#dfe6ec 40%,#a9b8c4 100%)"></section>
<h2 class="section-title" style="top:3200px">Volunteer With Us</h2>
<div class="underline" style="top:3264px"></div>
<p class="abs" style="left:210px;top:3290px;width:780px;text-align:center;font-size:16px;line-height:1.5">Volunteering with Coastline Stillness is a simple way to give back while growing within a supportive community. Whether you help with meditation sessions, events, outreach, or behind-the-scenes support, your time and presence help create calm, welcoming spaces for others. No special skills are required — just a genuine willingness to contribute and connect.</p>
<span class="btn" style="left:487px;top:3440px">Become a Volunteer</span>

<!-- About -->
<h2 class="abs" style="left:110px;top:3880px;font-size:44px;font-weight:700;color:var(--ink)">About Us</h2>
<div class="abs" style="left:110px;top:3944px;width:60px;height:4px;background:var(--tan)"></div>
<p class="abs" style="left:110px;top:3976px;width:440px;font-size:15px;line-height:1.65">Welcome to Veluna Meditation Australia - your bright, bubbly oasis of calm in the vast digital desert. Kick off your shoes, find your favourite comfy spot, and prepare to embark on a life-changing journey to improved health, wellness, and spiritual awakening, all served with a sprinkle of playfulness and a dash of joy.</p>
<p class="abs" style="left:110px;top:4150px;width:440px;font-size:15px;line-height:1.65">The practice is taught freely in a calm, supportive environment and is suitable for people of all ages and backgrounds.</p>
<span class="btn" style="left:110px;top:4260px">Read More</span>
<div class="abs" role="img" aria-label="Illustration of a woman meditating among flowers" style="left:610px;top:3880px;width:480px;height:460px;border-radius:8px;background:linear-gradient(160deg,#3e5f3a,#c57a3d)"></div>

<!-- Footer -->
<footer class="footer">
  <h4 style="left:110px;top:50px">Stay Connected</h4>
  <p class="abs" style="left:110px;top:84px;width:340px;font-size:14px;line-height:1.5">Gentle updates from our meditation community. Mindful updates on sessions and events.</p>
  <div class="abs" style="left:530px;top:64px;width:400px;height:40px;border:1px solid #777;border-radius:20px;font-size:13px;color:#ccc;padding:11px 20px">Email Address</div>
  <span class="btn" style="left:948px;top:64px">Subscribe</span>
  <div class="rule" style="top:150px"></div>

  <h4 style="left:110px;top:176px">About Us</h4>
  <p class="abs" style="left:110px;top:216px;width:190px;font-size:13px;line-height:1.6">Coastline Stillness is a not-for-profit organisation sharing a simple, natural meditation practice rooted in the Himalayan tradition.</p>
  <span class="abs" style="left:110px;top:338px;width:34px;height:34px;border-radius:50%;background:var(--green)"></span>
  <span class="abs" style="left:156px;top:338px;width:34px;height:34px;border-radius:50%;border:2px solid #fff"></span>

  <h4 style="left:400px;top:176px">Main Links</h4>
  <div class="col" style="left:400px;top:212px">Home<br>Coastline Stillness<br>Meditation Sessions<br>Events &amp; Programs<br>About the Organisation</div>

  <h4 style="left:640px;top:176px">Contact Us</h4>
  <svg class="abs" style="left:640px;top:222px" width="18" height="150" viewBox="0 0 18 150" fill="none" stroke="#ccc" stroke-width="1.6">
    <path d="M9 2c-3.5 0-6 2.6-6 6 0 4.5 6 10 6 10s6-5.5 6-10c0-3.4-2.5-6-6-6z"/><circle cx="9" cy="8" r="2"/>
    <path d="M4 62l3-3 3 4-2 2c1 2 3 4 5 5l2-2 4 3-3 3c-6-1-11-6-12-12z"/>
    <rect x="2" y="112" width="14" height="10" rx="1"/><path d="M2 113l7 5 7-5"/>
  </svg>
  <div class="col" style="left:672px;top:220px;line-height:1.5;width:190px">48 Wattle Grove Lane, Ridgeview, Victoria 3999</div>
  <div class="col" style="left:672px;top:272px">+61 400 000 123</div>
  <div class="col" style="left:672px;top:322px">hello@velunameditation.org.au</div>

  <h4 style="left:980px;top:176px">Other Links</h4>
  <div class="col" style="left:980px;top:212px">Resources<br>Contact Us<br>Volunteer<br>Donate<br>Privacy Policy</div>

  <div class="rule" style="top:480px"></div>
  <p class="abs" style="left:0;width:1200px;top:508px;text-align:center;font-size:13px">Copyright © 2024 Veluna Meditation Australia. All rights reserved.</p>
</footer>

</body>
</html>
```